Morvela Aesthetic Doctor

I require an elegant, luxurious looking business card for my aesthetic business. I am a doctor and that will set me aside from competitors. I am planning to provide home and spa based treatments to clients with high expectations. I have attached my logo.

```html
<!DOCTYPE html>
<html lang="en">
<head>
<meta charset="utf-8">
<title>Morvela Aesthetic Doctor – Business Card</title>
<link href="https://fonts.googleapis.com/css2?family=Marcellus&family=Open+Sans:wght@400;600;700&display=swap" rel="stylesheet">
<style>
  :root {
    --backdrop: #1c1c1e;
    --card-light: #f7f8f9;
    --card-dark: #0b0b0c;
    --ink: #1e1e22;
    --sky: #4fa9e0;
    --sky-soft: #7cc3ec;
    --silver: #b9bcc0;
  }
  * { margin: 0; padding: 0; box-sizing: border-box; }
  html, body { width: 1200px; height: 900px; overflow: hidden; }
  body {
    background: var(--backdrop);
    font-family: "Open Sans", Arial, sans-serif;
    position: relative;
  }
  .card {
    position: absolute;
    left: 285px;
    width: 630px;
    height: 360px;
    border-radius: 26px;
  }
  .card--front { top: 70px; background: var(--card-light); color: var(--ink); }
  .card--back { top: 470px; background: var(--card-dark); }

  .holder { position: absolute; left: 52px; top: 44px; }
  .holder__name { font-size: 19px; font-weight: 700; letter-spacing: 0.02em; }
  .holder__post { font-size: 14px; font-weight: 400; }
  .holder__diploma { margin-top: 4px; font-size: 14px; color: var(--sky); letter-spacing: 0.02em; }

  .contact { position: absolute; left: 52px; top: 118px; list-style: none; }
  .contact li { display: flex; align-items: center; gap: 10px; font-size: 14px; line-height: 26px; }
  .contact svg { width: 14px; height: 14px; fill: var(--sky); }

  .services { position: absolute; left: 52px; top: 218px; color: var(--sky); font-size: 14.5px; line-height: 25px; }
  .services .sep { padding: 0 8px; }

  .wordmark {
    position: absolute; display: flex; align-items: center; gap: 14px;
    font-family: "Marcellus", Georgia, serif; font-weight: 400; line-height: 1.05;
    text-transform: uppercase;
  }
  .wordmark__ring { border-radius: 50%; border: 2px solid currentColor; flex: none; }
  .card--front .wordmark { right: 44px; bottom: 40px; color: var(--sky); }
  .card--front .wordmark__ring { width: 54px; height: 54px; }
  .card--front .wordmark__text { font-size: 30px; }
  .card--front .wordmark__text span { display: block; font-size: 17px; letter-spacing: 0.06em; }

  .card--back .wordmark { left: 0; right: 0; top: 0; bottom: 0; justify-content: center; color: var(--silver); gap: 26px; }
  .card--back .wordmark__ring { width: 150px; height: 150px; border-width: 3px; }
  .card--back .wordmark__text { font-size: 52px; }
  .card--back .wordmark__text span { display: block; font-size: 24px; letter-spacing: 0.06em; }
</style>
</head>
<body>
  <section class="card card--front">
    <header class="holder">
      <h1 class="holder__name">DR ELENA VOSS <span class="holder__post">MRCPCH MD</span></h1>
      <p class="holder__diploma">AUSTRALASIAN DIPLOMA OF AESTHETIC MEDICINE</p>
    </header>
    <ul class="contact">
      <li><svg viewBox="0 0 24 24"><path d="M6.6 10.8a15.1 15.1 0 0 0 6.6 6.6l2.2-2.2a1 1 0 0 1 1-.25 11.4 11.4 0 0 0 3.6.57 1 1 0 0 1 1 1V20a1 1 0 0 1-1 1A17 17 0 0 1 3 4a1 1 0 0 1 1-1h3.5a1 1 0 0 1 1 1c0 1.25.2 2.45.57 3.57a1 1 0 0 1-.25 1z"/></svg>0800 555 017</li>
      <li><svg viewBox="0 0 24 24"><path d="M2 5h20v14H2zM4 7v.4l8 5.2 8-5.2V7zm0 2.8V17h16V9.8l-8 5.2z"/></svg>elena@morvela.co.nz</li>
      <li><svg viewBox="0 0 24 24"><path d="M12 2a10 10 0 1 0 0 20 10 10 0 0 0 0-20zm6.9 6h-3a15 15 0 0 0-1.3-3.9A8 8 0 0 1 18.9 8zM12 4c.9 1.2 1.6 2.6 2 4h-4c.4-1.4 1.1-2.8 2-4zM4.3 14a8 8 0 0 1 0-4h3.4a16 16 0 0 0 0 4zm.8 2h3a15 15 0 0 0 1.3 3.9A8 8 0 0 1 5.1 16zm3-8h-3a8 8 0 0 1 4.3-3.9A15 15 0 0 0 8.1 8zM12 20c-.9-1.2-1.6-2.6-2-4h4c-.4 1.4-1.1 2.8-2 4zm2.3-6H9.7a14 14 0 0 1 0-4h4.6a14 14 0 0 1 0 4zm.3 5.9a15 15 0 0 0 1.3-3.9h3a8 8 0 0 1-4.3 3.9zm1.7-5.9a16 16 0 0 0 0-4h3.4a8 8 0 0 1 0 4z"/></svg>www.morvela.co.nz</li>
    </ul>
    <div class="services">
      <p>Dermal injectables<span class="sep">|</span>Plasma facials<span class="sep">|</span>Microneedling</p>
      <p>Skin boosters<span class="sep">|</span>Excessive sweating</p>
      <p>Home and Spa Based Treatments</p>
    </div>
    <div class="wordmark">
      <span class="wordmark__ring"></span>
      <p class="wordmark__text">Morvela<span>Aesthetic Doctor</span></p>
    </div>
  </section>

  <section class="card card--back">
    <div class="wordmark">
      <span class="wordmark__ring"></span>
      <p class="wordmark__text">Morvela<span>Aesthetic Doctor</span></p>
    </div>
  </section>
</body>
</html>
```